Webdesign für Gutshof
Zielgruppe
Gutshof Brandlinger:
Zielgruppe sind alle, die gern Fisch essen. Es gibt einen Hofladen, einen Partyservice, eine Gaststätte und eine kleine Pension. Wichtig wäre darzustellen, dass es in der Gaststätte außer Fisch auch Fleisch gibt.
Einen Einblick geben Ihnen die Webseite und der beiliegende Flyer.
Aufgabenstellung
Die Öffnungszeiten von Gaststätte und Hofladen sollten prominent dargestellt werden. Neben den eigenen Bildern sollen auch stock-Fotos genutzt werden.

```html
<!DOCTYPE html>
<html lang="de">
<head>
<meta charset="utf-8">
<title>Gutshof Brandlinger</title>
<link href="https://fonts.googleapis.com/css2?family=Kaushan+Script&family=Great+Vibes&family=Raleway:wght@300;400;600;700&display=swap" rel="stylesheet">
<style>
:root{
  --tan:#c69352;
  --ink:#222;
  --muted:#9a9a9a;
  --dark:#1b1a1a;
  --footer:#1f1e1e;
  --line:#e6e6e6;
  --white:#fff;
}
*{margin:0;padding:0;box-sizing:border-box}
html,body{width:1200px;height:4671px;overflow:hidden;background:var(--white)}
body{position:relative;font-family:'Raleway',sans-serif;color:var(--ink)}
.abs{position:absolute}
.script{font-family:'Great Vibes',cursive;color:var(--tan);font-weight:400}
.brush{font-family:'Kaushan Script',cursive;font-weight:400;color:var(--ink)}
.center{text-align:center}

/* hero */
.hero{left:0;top:0;width:1200px;height:660px;background:radial-gradient(ellipse at 50% 30%,#4a4440 0%,#2b2622 55%,#1a1614 100%)}
.hero-welcome{top:168px;width:1200px;font-size:42px;color:#fff}
.hero-title{top:210px;width:1200px;font-size:82px;color:#fff}
.hero-text{top:318px;left:200px;width:800px;font-size:15px;font-weight:700;line-height:25px;color:#fff}

/* section headings */
.kicker{width:1200px;font-size:28px}
.kicker-rule{left:522px;width:156px;height:2px;background:var(--tan)}

/* service cards */
.service{width:248px;text-align:center}
.service .photo{width:248px;height:165px}
.service .label{margin-top:20px;font-size:30px;line-height:34px}
.service .title{margin-top:6px;font-size:25px;line-height:28px}
.service .text{margin:14px auto 0;width:230px;font-size:12px;line-height:20px;color:var(--muted);font-weight:300}

/* feature rows */
.feature-text{width:523px;text-align:center}
.feature-text .label{font-size:36px;line-height:40px}
.feature-text .title{font-size:42px;line-height:50px;margin-top:2px}
.feature-text .orn{font-size:20px;color:var(--tan);margin-top:10px;letter-spacing:6px}
.feature-text p{margin:18px auto 0;width:470px;font-size:13px;line-height:23px;color:var(--muted);font-weight:300}
.btn{display:inline-block;margin-top:30px;width:160px;height:46px;line-height:42px;border:2px solid var(--tan);border-radius:24px;color:var(--tan);font-size:10px;font-weight:700;letter-spacing:.5px}

/* nav */
.nav{top:3480px;left:439px;display:flex;gap:30px;font-size:11px;font-weight:700;letter-spacing:.3px}
.nav-rule{top:3539px;left:0;width:1200px;height:1px;background:var(--line)}

/* blog cards */
.post{width:241px;height:461px;background:#fff;box-shadow:0 2px 14px rgba(0,0,0,.08)}
.post .photo{height:181px}
.post h3{margin:30px 28px 0;font-size:18px;line-height:26px;font-weight:700}
.post p{margin:22px 28px 0;font-size:12px;line-height:22px;color:var(--muted);font-weight:300}
.post .meta{margin:26px 28px 0;border-top:1px solid var(--line);padding-top:16px;font-size:9px;color:#666}

/* hours */
.hours{width:341px;height:339px;background:var(--dark);color:#ddd}
.hours .tab{position:absolute;left:130px;top:-20px}
.hours h4{margin-top:32px;text-align:center;font-family:'Kaushan Script',cursive;font-weight:400;font-size:26px;color:#fff}
.hours .sun{display:block;margin:10px auto 0}
.hours ul{list-style:none;margin:26px 38px 0}
.hours li{display:flex;justify-content:space-between;font-size:12px;line-height:33px;border-bottom:1px solid #333}

/* footer */
.address{top:4506px;width:1200px;font-size:12px;color:#333}
.footer{left:0;top:4585px;width:1200px;height:86px;background:var(--footer);color:#fff;font-size:11px}
.footer .bump{position:absolute;left:570px;top:-18px}
.footer span{position:absolute;top:35px}
</style>
</head>
<body>

<header>
  <div class="abs hero" role="img" aria-label="Dunkler Holztisch mit frischem Fisch, Zwiebelringen, Kräutern und Gewürzen"></div>
  <div class="abs hero-welcome script center">Herzlich Willkommen Im</div>
  <h1 class="abs hero-title brush center">Gutshof Brandlinger</h1>
  <p class="abs hero-text center">Lorem ipsum dolor sit amet, consetetur sadipscing elitr, sed diam nonumy eirmod tempor invidunt ut labore et dolore magna aliquyam erat, sed diam voluptua. At vero eos et accusam et</p>
</header>

<section>
  <h2 class="abs kicker script center" style="top:758px;font-size:30px">Unser Service</h2>
  <div class="abs kicker-rule" style="top:796px"></div>

  <article class="abs service" style="left:42px;top:834px">
    <div class="photo" role="img" aria-label="Gaststätte mit rotem Fachwerkgeländer" style="background:linear-gradient(160deg,#9fb2c4 0%,#d8cdb4 45%,#8a4a34 70%,#8a8f6a 100%)"></div>
    <div class="label script">Hofgaststätte</div>
    <div class="title brush">Genüßlich essen</div>
    <p class="text">Wir haben bei uns im Gutshof eine Wöchentlich Wechselnde Karte, mit Leckeren Fisch- und Fleischgerichte für Groß und Klein.</p>
  </article>
  <article class="abs service" style="left:319px;top:834px">
    <div class="photo" role="img" aria-label="Pensionszimmer mit violetten Vorhängen" style="background:linear-gradient(120deg,#5a3a6e 0%,#8a6a9c 45%,#c9b8c8 75%,#6b4d77 100%)"></div>
    <div class="label script">Pension</div>
    <div class="title brush">Hier finden Sie Ruhe</div>
    <p class="text">Wir verfügen über 2 Pensionszimmer mit Doppelbetten in denen Sie einmal vollkommen abschalten können.</p>
  </article>
  <article class="abs service" style="left:595px;top:834px">
    <div class="photo" role="img" aria-label="Hofladen mit beleuchtetem Schaufenster" style="background:linear-gradient(170deg,#b9c3cc 0%,#4a4a48 40%,#7a5a38 65%,#6e6e66 100%)"></div>
    <div class="label script">Hofladen</div>
    <div class="title brush">Wir beraten Sie gerne</div>
    <p class="text">In unserem Ortsansässigen Hofladen, finden Sie alles was Sie als Fischliebhaber begehren.</p>
  </article>
  <article class="abs service" style="left:871px;top:834px">
    <div class="photo" role="img" aria-label="Warmhaltebehälter mit Speisen am Buffet" style="background:linear-gradient(160deg,#1f4a44 0%,#6b7a74 40%,#b06a2c 70%,#2c3a36 100%)"></div>
    <div class="label script">Partyservice</div>
    <div class="title brush">Partys feiern mit Brandlingers</div>
    <p class="text">Mit unserem Partyservice, sind Sie bei jeder Party der Hit. Sie erhalten das Rund-um-Sorglospaket.</p>
  </article>
</section>

<section>
  <div class="abs feature-text" style="left:42px;top:1480px">
    <div class="label script">Hofgaststätte</div>
    <h2 class="title brush">Speisen wie die Fischer</h2>
    <div class="orn">» «</div>
    <p>Lorem ipsum dolor sit amet, consetetur sadipscing elitr, sed diam nonumy eirmod tempor invidunt ut labore et dolore magna aliquyam</p>
    <span class="btn">MEHR...</span>
  </div>
  <div class="abs" style="left:595px;top:1439px;width:523px;height:347px;background:linear-gradient(170deg,#3e4048 0%,#d9d0b8 35%,#8a3e2c 60%,#9a9a90 85%,#6c7a4a 100%)" role="img" aria-label="Eingang der Gaststätte mit Pflasterweg und Blumen"></div>

  <div class="abs" style="left:42px;top:1880px;width:524px;height:393px;background:radial-gradient(ellipse at 45% 35%,#c7a074 0%,#6e5036 45%,#2a1e16 100%)" role="img" aria-label="Gemachtes Bett mit gefalteten roten Handtüchern"></div>
  <div class="abs feature-text" style="left:595px;top:1903px">
    <div class="label script">Pension</div>
    <h2 class="title brush">Lorem ipsum dolor sit</h2>
    <div class="orn">» «</div>
    <p>Lorem ipsum dolor sit amet, consetetur sadipscing elitr, sed diam nonumy eirmod tempor invidunt ut labore et dolore magna aliquyam</p>
    <span class="btn">MEHR...</span>
  </div>

  <div class="abs feature-text" style="left:42px;top:2391px">
    <div class="label script">Hofladen</div>
    <h2 class="title brush">Lorem ipsum dolor</h2>
    <div class="orn">» «</div>
    <p>Lorem ipsum dolor sit amet, consetetur sadipscing elitr, sed diam nonumy eirmod tempor invidunt ut labore et dolore magna aliquyam</p>
    <span class="btn">MEHR...</span>
  </div>
  <div class="abs" style="left:595px;top:2370px;width:523px;height:397px;background:radial-gradient(ellipse at 50% 55%,#e8e4dc 0%,#5a1f24 40%,#1e1414 100%)" role="img" aria-label="Gläser mit selbstgemachtem Fruchtaufstrich"></div>

  <div class="abs" style="left:42px;top:2861px;width:524px;height:326px;background:linear-gradient(160deg,#d9a45c 0%,#f0e4cc 40%,#f6f2ea 60%,#5a4a3c 100%)" role="img" aria-label="Weiß eingedeckte Buffettafel mit Warmhaltebehältern"></div>
  <div class="abs feature-text" style="left:595px;top:2884px">
    <div class="label script">Partyservice</div>
    <h2 class="title brush">Lorem ipsum dolor sit</h2>
    <div class="orn">» «</div>
    <p>Lorem ipsum dolor sit amet, consetetur sadipscing elitr, sed diam nonumy eirmod tempor invidunt ut labore et dolore magna aliquyam</p>
    <span class="btn">MEHR...</span>
  </div>
</section>

<section>
  <h2 class="abs kicker script center" style="top:3400px;font-size:40px">Nicht Verpassen!</h2>
  <nav class="abs nav"><span>HOME</span><span>HOFGASTSTÄTTE</span><span>PENSION</span><span>HOFLADEN</span><span>PARTYSERVICE</span><span>ÜBER UNS</span><span>KONTAKT</span></nav>
  <div class="abs nav-rule"></div>

  <article class="abs post" style="left:56px;top:3573px">
    <div class="photo" role="img" aria-label="Schale Müsli mit Beeren und Mandeln" style="background:radial-gradient(circle at 45% 50%,#f2eee6 0%,#8a8a86 45%,#2e2e30 100%)"></div>
    <h3>Lorem ipsum dolor sit</h3>
    <p>Lorem ipsum dolor sit amet, consetetur sadipscing elitr, sed diam nonumy eirmod tempor invidunt ut labore et dolore magna aliquyam</p>
    <div class="meta">Feb 22, 2017</div>
  </article>
  <article class="abs post" style="left:325px;top:3573px">
    <div class="photo" role="img" aria-label="Pfanne mit Spiegeleiern und Tomaten" style="background:radial-gradient(circle at 50% 45%,#e8a040 0%,#5a4a40 45%,#1e1e1e 100%)"></div>
    <h3>Lorem ipsum dolor sit</h3>
    <p>Lorem ipsum dolor sit amet, consetetur sadipscing elitr, sed diam nonumy eirmod tempor invidunt ut labore et dolore magna aliquyam</p>
    <div class="meta">Feb 22, 2017</div>
  </article>
  <article class="abs post" style="left:594px;top:3573px">
    <div class="photo" role="img" aria-label="Brettchen mit Waffeln und Erdbeeren" style="background:radial-gradient(circle at 50% 55%,#c98a54 0%,#6a4a36 45%,#2a2220 100%)"></div>
    <h3>Lorem ipsum dolor sit</h3>
    <p>Lorem ipsum dolor sit amet, consetetur sadipscing elitr, sed diam nonumy eirmod tempor invidunt ut labore et dolore magna aliquyam</p>
    <div class="meta">Feb 22, 2017</div>
  </article>
  <article class="abs post" style="left:863px;top:3573px">
    <div class="photo" role="img" aria-label="Gegrilltes Fleisch mit Gemüse auf dunklem Tisch" style="background:radial-gradient(circle at 50% 50%,#b0502a 0%,#5a2e1e 45%,#1c1a18 100%)"></div>
    <h3>Lorem ipsum dolor sit</h3>
    <p>Lorem ipsum dolor sit amet, consetetur sadipscing elitr, sed diam nonumy eirmod tempor invidunt ut labore et dolore magna aliquyam</p>
    <div class="meta">Feb 22, 2017</div>
  </article>
</section>

<section>
  <div class="abs hours" style="left:42px;top:4108px">
    <svg class="tab" width="80" height="22" viewBox="0 0 80 22"><path d="M0 22 C20 22 22 0 40 0 C58 0 60 22 80 22 Z" fill="#1b1a1a"/></svg>
    <h4>Öffnungszeiten Hofladen</h4>
    <svg class="sun" width="14" height="14" viewBox="0 0 14 14"><circle cx="7" cy="7" r="3" fill="none" stroke="#777" stroke-width="1.2"/><path d="M7 0v2M7 12v2M0 7h2M12 7h2M2 2l1.5 1.5M10.5 10.5L12 12M2 12l1.5-1.5M10.5 3.5L12 2" stroke="#777" stroke-width="1"/></svg>
    <ul>
      <li><span>Dienstag</span><span>14:00 – 18:00</span></li>
      <li><span>Donnerstag</span><span>14:00 – 18:00</span></li>
      <li><span>Freitag</span><span>14:00 – 18:00</span></li>
      <li><span>Samstag</span><span>09:00 – 14:00</span></li>
      <li><span>Sonntag</span><span>09:00 – 11:00</span></li>
    </ul>
  </div>
  <div class="abs hours" style="left:779px;top:4108px">
    <svg class="tab" width="80" height="22" viewBox="0 0 80 22"><path d="M0 22 C20 22 22 0 40 0 C58 0 60 22 80 22 Z" fill="#1b1a1a"/></svg>
    <h4>Öffnungszeiten Gaststätte</h4>
    <svg class="sun" width="14" height="14" viewBox="0 0 14 14"><circle cx="7" cy="7" r="3" fill="none" stroke="#777" stroke-width="1.2"/><path d="M7 0v2M7 12v2M0 7h2M12 7h2M2 2l1.5 1.5M10.5 10.5L12 12M2 12l1.5-1.5M10.5 3.5L12 2" stroke="#777" stroke-width="1"/></svg>
    <ul>
      <li><span>Freitags</span><span>17:00 – 24:00</span></li>
      <li><span>Samstag</span><span>11:00 – 24:00</span></li>
      <li><span>Sonntag</span><span>11:00 – 14:00</span></li>
      <li><span>Feiertags</span><span>11:00 – 14:00</span></li>
      <li><span>Mo. - Fr.</span><span>nach Absprache</span></li>
    </ul>
  </div>
</section>

<footer>
  <p class="abs address center">Gutshof Brandlinger | Lindenweg 12 | 01234 Musterhain - Talberg | Tel.: 01234 / 567890 | mail@gutshof-brandlinger.de</p>
  <div class="abs footer">
    <svg class="bump" width="60" height="20" viewBox="0 0 60 20"><path d="M0 20 C15 20 16 0 30 0 C44 0 45 20 60 20 Z" fill="#1f1e1e"/></svg>
    <span style="left:505px">Impressum / Datenschutz</span>
    <span style="left:863px">Gutshof Brandlinger 0.2 © 2021</span>
  </div>
</footer>

</body>
</html>
```